Business Cards and Stationery for Mobile Ultrasound
Redfern Harbor Mobile Ultrasound
Business Cards and Stationery for Mobile Ultrasound - Medical
Creative Brief
Professional
Marovic Deltrane
P.O Box 827 Quenton CA 95871
mar@rhqx.example
rhqx.example

```html
<!DOCTYPE html>
<html lang="en">
<head>
<meta charset="utf-8">
<title>Redfern Harbor Mobile Ultrasound – Business Card</title>
<link rel="stylesheet" href="https://fonts.googleapis.com/css2?family=Open+Sans:wght@400;600&display=swap">
<style>
  :root {
    --stage: #3b3b3d;
    --green-light: #3fae3a;
    --green-dark: #1b7a22;
    --brand-green: #2f9a36;
    --purple: #5b2d86;
    --ink: #4a4a4a;
    --white: #ffffff;
  }
  * { margin: 0; padding: 0; box-sizing: border-box; }
  html, body { width: 1200px; height: 751px; overflow: hidden; }
  body {
    background: var(--stage);
    font-family: "Open Sans", Arial, sans-serif;
    position: relative;
  }
  .card {
    position: absolute;
    top: 225px;
    width: 520px;
    height: 300px;
    border-radius: 16px;
    overflow: hidden;
  }
  .card-front {
    left: 50px;
    background: radial-gradient(ellipse at 50% 40%, var(--green-light), var(--green-dark) 85%);
    color: var(--white);
  }
  .card-back {
    left: 630px;
    background: var(--white);
    color: var(--ink);
  }
  .brand {
    position: absolute;
    left: 0; right: 0;
    display: flex;
    align-items: center;
    justify-content: center;
    gap: 10px;
    font-weight: 600;
    text-align: center;
    line-height: 1.15;
  }
  .brand-dot {
    width: 14px; height: 14px;
    border-radius: 50%;
    background: currentColor;
    flex: none;
  }
  .card-front .brand { top: 108px; font-size: 22px; }
  .front-web {
    position: absolute;
    top: 200px; left: 0; right: 0;
    text-align: center;
    font-size: 10px;
    letter-spacing: 3px;
  }
  .card-back .brand { top: 128px; font-size: 20px; color: var(--brand-green); }
  .side-band {
    position: absolute;
    left: 0; top: 40px;
    width: 8px; height: 70px;
    background: var(--purple);
  }
  .holder {
    position: absolute;
    left: 24px; top: 44px;
  }
  .holder-name {
    font-size: 15px;
    font-weight: 600;
    color: var(--purple);
  }
  .holder-address {
    margin-top: 4px;
    font-size: 9.5px;
    line-height: 1.5;
  }
  .contact-list {
    position: absolute;
    right: 0; top: 120px;
    list-style: none;
  }
  .contact-list li {
    display: flex;
    align-items: center;
    justify-content: flex-end;
    gap: 8px;
    height: 18px;
    font-size: 9.5px;
  }
  .contact-icon {
    width: 14px; height: 14px;
    background: var(--purple);
    display: flex; align-items: center; justify-content: center;
  }
  .contact-list li:nth-child(2) .contact-icon { background: var(--brand-green); }
  .contact-icon svg { width: 9px; height: 9px; fill: var(--white); }
</style>
</head>
<body>
  <section class="card card-front">
    <div class="brand"><span class="brand-dot"></span><span>Redfern Harbor<br>Mobile Ultrasound</span></div>
    <p class="front-web">www.rhqx.example</p>
  </section>

  <section class="card card-back">
    <div class="side-band"></div>
    <div class="holder">
      <p class="holder-name">Marovic Deltrane</p>
      <p class="holder-address">P.O Box 827<br>Quenton CA 95871</p>
    </div>
    <div class="brand"><span class="brand-dot"></span><span>Redfern Harbor<br>Mobile Ultrasound</span></div>
    <ul class="contact-list">
      <li>555-014-2290
        <span class="contact-icon"><svg viewBox="0 0 10 10"><path d="M2 0.5 L3.8 2.6 3 3.8 C3.6 5 5 6.4 6.2 7 L7.4 6.2 9.5 8 8.4 9.5 C4.5 9.2 0.8 5.5 0.5 1.6 Z"/></svg></span>
      </li>
      <li>mar@rhqx.example
        <span class="contact-icon"><svg viewBox="0 0 10 10"><path d="M0.5 2 H9.5 V8 H0.5 Z M0.5 2 L5 5.5 9.5 2" fill="none" stroke="#fff" stroke-width="1"/></svg></span>
      </li>
      <li>www.rhqx.example
        <span class="contact-icon"><svg viewBox="0 0 10 10"><circle cx="5" cy="5" r="4" fill="none" stroke="#fff" stroke-width="1"/><path d="M1 5 H9 M5 1 C3 3.5 3 6.5 5 9 M5 1 C7 3.5 7 6.5 5 9" fill="none" stroke="#fff" stroke-width="0.8"/></svg></span>
      </li>
    </ul>
  </section>
</body>
</html>
```